Magician | Speaker looks for an innovative business card design

I'm a magician and public speaker offering artistic and modern magical experiences.
I'm based in Brussels (Belgium.) I love magic performed up-close, creating a space of intimacy, even when I'm on stage.
The final design should communicate professionalism, elegance, artistry, and a friendly kind personality

I would like to see designs based either on my photos and/or the way I sign my name Remy Vok (see attached files for more info.)
Additional photos and more info about what I offer can be seen at www.remy-vok.net

My current business card design is also attached. I like the fact that the reverse of my current design includes quotes from master magicians about magic, changing the way my participants see the art of magic.

Note: I would like a double-sided card design. However, I need white space on the reverse to be able to write things on for my performances.

Details to include on the card:
Artist name: Remy Vok
Offer: magician + (public) speaker or magic + (public) speaking (the + sign can be replaced by another character, like a bullet or a pipe)
Phone: +32 471 265 903
Email: book@remy-vok.net
(optional) Website: www.remy-vok.net or remy-vok.net

Target Market(s)

Corporate, organisations, companies as well as individuals

Industry/Entity Type

Artists

Colors

Designer to choose colors to be used in the design.

Requirements
Nice to have
• A side with a mirror could be nice

```html
<!DOCTYPE html>
<html lang="en">
<head>
<meta charset="utf-8">
<title>Remy Vok – business card, front and reverse</title>
<link rel="stylesheet" href="https://fonts.googleapis.com/css2?family=Yellowtail&family=Roboto:wght@300;400&display=block">
<style>
  :root {
    --backdrop: #c0c1c3;
    --card-front: #000000;
    --card-back: #ffffff;
    --name-silver: #a9a9ab;
    --rule-silver: #a3a3a6;
    --contact-grey: #b8b8b8;
    --web-grey: #8e8e8e;
    --quote-ink: #1a1a1a;
  }
  html, body {
    margin: 0;
    padding: 0;
    width: 1200px;
    height: 1021px;
    overflow: hidden;
    background: var(--backdrop);
  }
  .card-sheet {
    display: block;
    width: 1200px;
    height: 1021px;
  }
  .card-front-shape { fill: var(--card-front); }
  .card-back-shape { fill: var(--card-back); }
  .artist-name {
    font-family: "Yellowtail", "Brush Script MT", cursive;
    font-size: 52px;
    fill: var(--name-silver);
  }
  .artist-offer {
    font-family: "Yellowtail", "Brush Script MT", cursive;
    font-size: 29px;
    fill: var(--name-silver);
  }
  .offer-rule { fill: var(--rule-silver); }
  .contact-line {
    font-family: "Roboto", Arial, sans-serif;
    font-weight: 300;
    font-size: 16px;
    fill: var(--contact-grey);
  }
  .website-line {
    font-family: "Roboto", Arial, sans-serif;
    font-weight: 300;
    font-size: 16px;
    fill: var(--web-grey);
  }
  .quote-line {
    font-family: "Roboto", Arial, sans-serif;
    font-weight: 300;
    font-size: 15px;
    fill: var(--quote-ink);
  }
  .quote-line-wide { word-spacing: 8px; }
  .quote-line-mid { word-spacing: 5px; }
  .quote-author {
    font-family: "Roboto", Arial, sans-serif;
    font-weight: 300;
    font-size: 15px;
    fill: var(--quote-ink);
  }
  .quote-author-role {
    font-family: "Roboto", Arial, sans-serif;
    font-weight: 300;
    font-size: 12px;
    fill: var(--quote-ink);
  }
  .quote-rule { stroke: var(--quote-ink); stroke-width: 1; }
</style>
</head>
<body>
<svg class="card-sheet" viewBox="0 0 1200 1021" xmlns="http://www.w3.org/2000/svg" aria-label="Remy Vok business card, front and reverse">

  <g class="card-front">
    <path class="card-front-shape" d="M313,245 Q313,205 353,201 L845,158 Q886,155 886,196 L886,474 Q886,510 850,510 L349,510 Q313,510 313,474 Z"/>
    <text class="artist-name" x="839" y="252" text-anchor="end">Remy Vok</text>
    <text class="artist-offer" x="839" y="330" text-anchor="end">magician - speaker</text>
    <rect class="offer-rule" x="600" y="348" width="239" height="12"/>
    <text class="contact-line" x="839" y="421" text-anchor="end">+32 471 265 903</text>
    <text class="contact-line" x="839" y="442" text-anchor="end">book@remy-vok.net</text>
    <text class="website-line" transform="translate(384,472) rotate(-90)" x="0" y="0">www.remy-vok.net or remy-vok.net</text>
  </g>

  <g class="card-back">
    <path class="card-back-shape" d="M313,576 Q313,537 352,540 L846,585 Q886,590 886,628 L886,854 Q886,890 850,890 L349,890 Q313,890 313,854 Z"/>
    <g class="quote-block" transform="translate(726,866) rotate(-90)">
      <text class="quote-line quote-line-wide" x="0" y="0">“Wonder is not about tricking and</text>
      <text class="quote-line quote-line-mid" x="0" y="22">puzzling people. It is about giving</text>
      <text class="quote-line" x="0" y="44">them curiosity, joy and surprise.”</text>
      <text class="quote-author" x="0" y="84">NOEL BRANDT</text>
      <text class="quote-author-role" x="0" y="98">Master magician</text>
      <line class="quote-rule" x1="152" y1="78" x2="266" y2="78"/>
    </g>
  </g>
</svg>
</body>
</html>
```